PPT/PDF of Tourism related Brand Value Proposition

I have already created a PPT but want a slicker, more compelling design.
This PPT connects the brand value proposition of the Tarvellan Meetings Office to the brand architecture and language of its mother-brand, Velora Haven and its tagline "Always Velora". Both the Orvanta Travel site (http://www.orvanta-travel.net/) and the specific site for the Tarvellan Meetings Office (http://www.tarvellan-meetings.net/ should be consulted as reference points. Orvanta Travel presents Slovenia as a destination for all markets while the Tarvellan Meetings Office aims specifically at business tourism (Conventions, Meetings, Events etc). The final PPT as a PFD will be used to present the new brand messaging to the Board of the Meetings Office

Target Market(s)

Internal presentation to the Board of the Tarvellan Meetings Office.

Industry/Entity Type

Tourism

Font styles to use
Sans Serif

Colors
33b8a4
acd036

Requirements
Must have
• Slick, professional visual appeal using the existing brand elements of the Tarvellan Meetings Office (see site above);
• Easy readability that highlights the language / messaging but connects the story with the image that it describes
• Consistency throughout

```html
<!DOCTYPE html>
<html lang="en">
<head>
<meta charset="utf-8">
<title>Key Words</title>
<link rel="stylesheet" href="https://fonts.googleapis.com/css2?family=Roboto+Condensed:wght@400;700&display=swap">
<style>
  :root {
    --brand-green: #78b852;
    --teal: #33b8a4;
    --lime: #acd036;
    --charcoal: #333333;
    --ink: #2b3a22;
    --white: #ffffff;
    --stage-dark: #121212;
    --stage-mid: #262626;
  }
  * { margin: 0; padding: 0; box-sizing: border-box; }
  html, body { width: 1200px; height: 900px; overflow: hidden; background: #000; }
  body { font-family: "Roboto Condensed", "Arial Narrow", sans-serif; }

  .slide {
    position: relative;
    width: 1200px;
    height: 900px;
    overflow: hidden;
  }
  .slide-backdrop {
    position: absolute;
    inset: 0;
    background: radial-gradient(ellipse at 45% 55%, var(--stage-mid) 0%, var(--stage-dark) 70%, #080808 100%);
  }

  .title-bar {
    position: absolute;
    left: 0; top: 0;
    width: 1200px; height: 81px;
    background: var(--brand-green);
    border-bottom: 2px solid #9fd27e;
  }
  .title-pointer {
    position: absolute;
    left: 45px; top: 81px;
    width: 30px; height: 18px;
  }
  .slide-title {
    position: absolute;
    left: 14px; top: 10px;
    color: var(--white);
    font-weight: 700;
    font-size: 48px;
    letter-spacing: -0.5px;
  }
  .brand-name {
    position: absolute;
    right: 24px; top: 14px;
    color: var(--white);
    font-weight: 700;
    font-size: 44px;
  }

  .keyword {
    position: absolute;
    width: 201px; height: 201px;
    margin: -100.5px 0 0 -100.5px;
    border-radius: 50%;
    border: 4.5px solid var(--white);
    display: flex;
    align-items: center;
    justify-content: center;
    text-align: center;
    color: var(--white);
    font-weight: 700;
    font-size: 25.5px;
    line-height: 38px;
    text-transform: uppercase;
  }
  .keyword--green { background: var(--brand-green); }
  .keyword--teal { background: var(--teal); }
  .keyword--lime { background: var(--lime); }
  .keyword--charcoal { background: var(--charcoal); }
  .keyword .lower { text-transform: none; }

  .footer-bar {
    position: absolute;
    left: 0; bottom: 0;
    width: 1200px; height: 42px;
    background: var(--brand-green);
  }
  .copyright {
    position: absolute;
    left: 8px; top: 7px;
    color: var(--ink);
    font-size: 24px;
  }
  .page-number {
    position: absolute;
    left: 1138px; top: 842px;
    width: 52px; height: 52px;
    border-radius: 50%;
    background: var(--ink);
    border: 3px solid var(--brand-green);
    color: var(--brand-green);
    font-size: 22px;
    display: flex;
    align-items: center;
    justify-content: center;
  }
</style>
</head>
<body>
  <main class="slide">
    <div class="slide-backdrop" role="img" aria-label="Dimmed photograph of rows of empty conference chairs"></div>

    <header class="title-bar">
      <h1 class="slide-title">Key Words</h1>
      <div class="brand-name">tovarin</div>
    </header>
    <svg class="title-pointer" viewBox="0 0 30 18" aria-hidden="true">
      <polygon points="0,0 30,0 15,17" fill="#78b852" stroke="#9fd27e" stroke-width="2"/>
      <rect x="0" y="0" width="30" height="2" fill="#78b852"/>
    </svg>

    <section class="keywords">
      <div class="keyword keyword--green" style="left:204px;top:291px">Organic<br>Development</div>
      <div class="keyword keyword--teal" style="left:474px;top:291px">Unspoilt<br>Nature</div>
      <div class="keyword keyword--lime" style="left:736px;top:291px">Authenticity</div>
      <div class="keyword keyword--charcoal" style="left:993px;top:291px">Calmness<br>of Nature</div>

      <div class="keyword keyword--teal" style="left:339px;top:468px"><span>Diligence <span class="lower">of</span><br>Slovenians</span></div>
      <div class="keyword keyword--green" style="left:601px;top:468px">Peace of<br>Mind</div>
      <div class="keyword keyword--teal" style="left:865px;top:468px">Preserve<br>Nature</div>

      <div class="keyword keyword--green" style="left:204px;top:648px">Organic<br>Development</div>
      <div class="keyword keyword--lime" style="left:474px;top:648px">Organic<br>Development</div>
      <div class="keyword keyword--teal" style="left:736px;top:648px">Organic<br>Development</div>
      <div class="keyword keyword--green" style="left:993px;top:648px">Organic<br>Development</div>
    </section>

    <footer class="footer-bar">
      <p class="copyright">Copyright text here</p>
    </footer>
    <div class="page-number">01</div>
  </main>
</body>
</html>
```